Plinthmoor Assessments Landing Page

We need a landing page re-designed for a new website www.plinthmoorassessments.example and the website is live if you search the address provided.
We need the industry standard files for embedding this into the landing page of our website. The company is a real estate advisory firm, we provide professional property services and are focused on business rates (commercial property taxation in the UK).
We have uploaded a file which is meant to provide a visual guide as to how we envisage the landing page looking. You are free to come up with an entirely different creative design. The image at the top with the search button is taken from another website so the design will need to be distinctly different but may follow the same theme. Furthermore, the colour palette does not need to be followed slavishly and can be modified changed and improved upon. It might be that you want to incorporate other visual cues such as a desktop PC, laptop and iPad as these are devices the website will be accessed from; however, this is not essential and only a guide.
**To clarify, please note, the target industry is commercial properties and not residential or domestic property, so please when incorporating designs of buildings its important to focus on commercial property such as shops, offices, industrial buildings etc.**
Target Market(s)
Occupiers of commercial real estate in the UK who pay property tax to occupy the property.
Look and feel
Each slider illustrates characteristics of the customer's brand and the style your logo design should communicate.

```html
<!DOCTYPE html>
<html lang="en">
<head>
<meta charset="utf-8">
<title>Plinthmoor Assessments</title>
<link href="https://fonts.googleapis.com/css2?family=Lato:wght@400;700;900&display=swap" rel="stylesheet">
<style>
:root{
  --orange:#d24a10;
  --blue:#1479b0;
  --ink:#2d2d2d;
  --muted:#555;
  --card:#e0edf5;
  --footer:#2c2e34;
  --night:#2e3a6a;
}
*{margin:0;padding:0;box-sizing:border-box}
html,body{width:1200px;height:3379px;overflow:hidden;background:#fff}
body{position:relative;font-family:'Lato',sans-serif;color:var(--ink)}
.abs{position:absolute}
.top-strip{left:0;top:0;width:1200px;height:22px;background:var(--blue)}
.brand{left:151px;top:56px;display:flex;align-items:center;gap:10px;font-weight:700;font-size:15px;color:#222;letter-spacing:.5px;text-transform:uppercase}
.brand-mark{width:22px;height:22px;background:var(--orange)}
.nav{top:64px;left:0;font-size:10.5px;font-weight:700;letter-spacing:.3px;color:#222}
.nav a{position:absolute;color:inherit;text-decoration:none;white-space:nowrap}
.nav a.active{color:#999;font-weight:400}
.nav-underline{left:439px;top:108px;width:75px;height:4px;background:var(--blue)}
.login{left:948px;top:54px;width:101px;height:35px;background:var(--orange);color:#fff;font-size:11px;font-weight:700;display:flex;align-items:center;justify-content:center}
.hero{left:0;top:112px;width:1200px;height:487px;background:linear-gradient(180deg,#3f4d86 0%,#2f3b6b 45%,#273257 70%,#3a4570 100%)}
.hero-title{left:214px;top:284px;width:800px;color:#fff;font-size:40px;font-weight:700;line-height:46px;letter-spacing:-.5px}
.hero-title .hot{color:#e0141e}
.hero-sub{left:214px;top:396px;color:#fff;font-size:19px}
.search{left:244px;top:557px;width:711px;height:74px;background:var(--blue);padding:9px}
.search-field{position:absolute;left:9px;top:9px;width:470px;height:56px;background:#fff;display:flex;align-items:center;padding-left:52px;font-size:17px;color:#555}
.search-field svg{position:absolute;left:25px;top:16px}
.search-btn{position:absolute;left:480px;top:9px;width:222px;height:56px;background:var(--orange);color:#fff;font-size:12px;font-weight:700;display:flex;align-items:center;justify-content:center}
.feature{width:212px;font-size:10.5px;line-height:21px;color:#333}
.feature em{color:var(--orange);font-style:normal}
.icon{top:721px}
.divider{left:574px;top:1063px;width:52px;height:3px;background:var(--orange)}
.photo{background:linear-gradient(135deg,#9aa6c2,#5d6888 55%,#3e4660)}
.about-text{left:581px;top:1158px;width:470px;font-size:12.5px;line-height:24px;color:#444}
.about-text em,.covered-text em{color:var(--orange);font-style:normal}
.h2{width:1200px;left:0;text-align:center;color:var(--orange);font-size:24px;font-weight:700}
.covered-text{left:151px;top:1578px;width:900px;font-size:15.5px;line-height:22.5px;color:#333}
.btn{background:var(--orange);color:#fff;font-size:12px;font-weight:700;display:flex;align-items:center;justify-content:center}
.stats{left:150px;top:1835px;width:899px;height:299px;background:linear-gradient(180deg,#232633 0%,#30344a 55%,#3b3350 75%,#1d1f2a 100%)}
.stat-ring{width:124px;height:124px;border:3px solid #fff;border-radius:50%;display:flex;align-items:center;justify-content:center;color:#fff;font-size:36px;font-weight:700;top:1922px}
.stat-label{top:2060px;width:300px;text-align:center;color:#fff;font-size:15px;font-weight:700}
.card{width:329px;height:209px;background:var(--card)}
.card-name{position:absolute;left:0;width:329px;top:24px;text-align:center;font-size:19px;color:#222}
.card-role{position:absolute;left:0;width:329px;top:49px;text-align:center;font-size:10px;color:#333}
.card-role em{color:var(--orange);font-style:normal}
.card-text{position:absolute;left:72px;top:68px;width:200px;font-size:10px;line-height:21px;color:#222}
.card-more{position:absolute;right:62px;top:170px;font-size:10px;color:var(--orange)}
.avatar{width:106px;height:106px;border-radius:50%;border:3px solid #fff;background:linear-gradient(160deg,#8a6a55,#3d2f28)}
.view-all{left:1007px;top:2772px;font-size:10px;color:var(--orange);text-decoration:underline}
.book-title{top:2855px;font-size:25px;font-weight:400;letter-spacing:.5px}
.footer{left:0;top:3040px;width:1200px;height:300px;background:var(--footer)}
.foot-links{left:151px;top:3076px;color:#fff;font-size:12.5px;font-weight:700;line-height:16px}
.foot-links p{margin-bottom:8px}
.foot-links .addr{font-weight:400;margin-top:-8px}
.foot-links .social{font-size:10.5px;display:flex;align-items:center;gap:5px;margin:0 0 3px}
.form{left:770px;top:3054px;width:279px;height:268px;background:#24262b}
.form-title{position:absolute;top:10px;width:279px;text-align:center;color:#fff;font-size:11.5px;font-weight:700}
.field{position:absolute;left:17px;width:246px;background:#fff;font-size:12.5px;color:#555;padding:11px 15px}
.submit{position:absolute;top:244px;width:279px;text-align:center;color:#fff;font-size:11.5px;font-weight:700}
.bottom-bar{left:0;top:3340px;width:1200px;height:39px;background:var(--blue);color:#fff;font-size:11px;font-weight:700;display:flex;align-items:center;justify-content:center;letter-spacing:.3px}
</style>
</head>
<body>
<div class="abs top-strip"></div>

<header>
  <div class="abs brand"><span class="brand-mark"></span>Plinthmoor Assessments</div>
  <nav class="abs nav">
    <a class="active" style="left:461px">HOME</a>
    <a style="left:530px">PROPERTY SEARCH</a>
    <a style="left:663px">DISCOVER</a>
    <a style="left:752px">ABOUT US</a>
    <a style="left:842px">MY ACCOUNT</a>
  </nav>
  <div class="abs nav-underline"></div>
  <div class="abs login">LOG IN</div>
</header>

<section>
  <div class="abs hero" role="img" aria-label="Night skyline of commercial office towers reflected in water"></div>
  <h1 class="abs hero-title">DO YOU THINK YOUR BUSINESS RATES ARE TOO <span class="hot">HIGH</span>?</h1>
  <p class="abs hero-sub">Use our free valuation tool or book a valuation with one of our qualified surveyors</p>
  <div class="abs search">
    <div class="search-field">
      <svg width="16" height="22" viewBox="0 0 16 22"><path d="M8 0C3.6 0 0 3.5 0 7.9 0 13.8 8 22 8 22s8-8.2 8-14.1C16 3.5 12.4 0 8 0zm0 11a3 3 0 110-6 3 3 0 010 6z" fill="#555"/></svg>
      Enter Your Commercial Property Postcode
    </div>
    <div class="search-btn">START FREE VALUATION NOW</div>
  </div>
</section>

<section>
  <svg class="abs icon" style="left:218px" width="72" height="72" viewBox="0 0 72 72" fill="none" stroke="#d24a10" stroke-width="2"><rect x="8" y="8" width="52" height="62"/><rect x="14" y="2" width="52" height="62" fill="#fff"/><circle cx="38" cy="26" r="12"/><path d="M38 14v12h12"/><path d="M22 46h30M22 52h30M22 58h20"/></svg>
  <svg class="abs icon" style="left:566px" width="66" height="72" viewBox="0 0 66 72" fill="none" stroke="#d24a10" stroke-width="2"><rect x="2" y="4" width="62" height="66"/><circle cx="14" cy="20" r="4"/><circle cx="14" cy="36" r="4"/><circle cx="14" cy="52" r="4"/><path d="M24 20h30M24 36h30M24 52h30"/></svg>
  <svg class="abs icon" style="left:910px" width="72" height="72" viewBox="0 0 72 72" fill="none" stroke="#d24a10" stroke-width="2"><rect x="2" y="8" width="56" height="50"/><path d="M2 20h56M14 2v12M46 2v12M10 28h40M10 38h40M10 48h30M20 28v24M30 28v24M40 28v20"/><circle cx="54" cy="54" r="13" fill="#fff"/><path d="M47 54l5 5 9-9"/></svg>

  <p class="abs feature" style="left:151px;top:824px">We take pride in ourselves on working collaboratively with our clients. That's why we offer a <em>Free Online Valuation Tool</em> which will help you better understand your rateable valuation and rates payable. We advise checking the factual data shown on the summary Valuation Breakdown with what is actually on the ground at your property, measuring it at all floor levels, noting the size and any other property features.</p>
  <p class="abs feature" style="left:494px;top:824px">Use our free valuation tool to estimate the rateable value of your commercial property in England and Wales. You can add, remove or aler the property information, make allowances and set the base rate pricing. At the end we will provide an estimate of the amount of rates payable and any potential savings.</p>
  <p class="abs feature" style="left:841px;top:824px">Need help? Book a qualified surveyor to advise you on the rateable value of your commercial property. You can book an essential desktop based valuation or a detailed on-sote valuation. Our surveyors are not driven by high commissions and will give you an honest fair assessmnt of your rateable valuation, rates payable and advise you on whether you should commence the</p>
  <div class="abs divider"></div>
</section>

<section>
  <div class="abs photo" style="left:150px;top:1132px;width:389px;height:254px" role="img" aria-label="Two business professionals reviewing documents in a high-rise office lounge"></div>
  <p class="abs about-text">Our fees are fixed up front, ensuring there are no surprises and we promise to <em>never charge any schock commissions</em>. Not only does this provide you with confidence that our serveyors are not lead by the prospect of large commissionpayments. We are here from the initial point of contact right through to the end, be there to provide an essential desktop valuation, on-site valuation or helping you through the Check, Challenge and Appeal process. We're here to support and guide you every step of the way.Our surveyors don't do speculatives appeals, we provide honest and professional advice at a <em>Fair Fixed Fee.</em></p>
</section>

<section>
  <h2 class="abs h2" style="top:1505px">We’ve got you covered!</h2>
  <p class="abs covered-text">Our rating list contains the most up-to-date information of around 2 million commercial properties in England and Wales. Our qualified rating surveyos provide nation-wide coverage and we employ some of the highest qualified surveyors with some holding the <em>Chartered Rating Diploma</em>.</p>
  <div class="abs btn" style="left:488px;top:1683px;width:224px;height:61px">START FREE VALUATION NOW</div>
</section>

<section>
  <div class="abs stats" role="img" aria-label="City skyline at night with a lit bridge over a river"></div>
  <div class="abs stat-ring" style="left:225px">2M</div>
  <div class="abs stat-ring" style="left:537px">10+</div>
  <div class="abs stat-ring" style="left:851px">100%</div>
  <div class="abs stat-label" style="left:137px">LISTED PROPERTIES</div>
  <div class="abs stat-label" style="left:449px">YEARS OF EXPERIENCE</div>
  <div class="abs stat-label" style="left:763px">CUSTOMER SATISFICATION</div>
</section>

<section>
  <h2 class="abs h2" style="top:2229px">Hear them!</h2>

  <div class="abs card" style="left:219px;top:2308px">
    <div class="card-name">Clara Wendell</div>
    <div class="card-role">CEO of <em>Banbury Footwear</em></div>
    <p class="card-text">Lorem ipsum dolor sit amet, consectetur adipisicing elit, sed do eiusmod tempor incididunt ut labore et dolore magna quis aliqua. Ut enim ad minim veniam, quis nostrud exercitation ullamco laboris nisi ...</p>
    <div class="card-more">Read all</div>
  </div>
  <div class="abs avatar" style="left:150px;top:2360px" role="img" aria-label="Portrait of Clara Wendell"></div>

  <div class="abs card" style="left:720px;top:2308px">
    <div class="card-name">Freya Oakes</div>
    <div class="card-role">Owner of <em>Kestrel Cafe</em></div>
    <p class="card-text">Lorem ipsum dolor sit amet, consectetur adipisicing elit, sed do eiusmod tempor incididunt ut labore et dolore magna quis aliqua. Ut enim ad minim veniam, quis nostrud exercitation ullamco laboris nisi ...</p>
    <div class="card-more">Read all</div>
  </div>
  <div class="abs avatar" style="left:650px;top:2360px;background:linear-gradient(160deg,#c9a878,#6b5040)" role="img" aria-label="Portrait of Freya Oakes"></div>

  <div class="abs card" style="left:219px;top:2551px">
    <div class="card-name">Theo Aldridge</div>
    <div class="card-role">Founder of <em>Hollin Legal</em></div>
    <p class="card-text">Lorem ipsum dolor sit amet, consectetur adipisicing elit, sed do eiusmod tempor incididunt ut labore et dolore magna quis aliqua. Ut enim ad minim veniam, quis nostrud exercitation ullamco laboris nisi ...</p>
    <div class="card-more">Read all</div>
  </div>
  <div class="abs avatar" style="left:150px;top:2603px;background:linear-gradient(160deg,#7a5a45,#2a201c)" role="img" aria-label="Portrait of Theo Aldridge"></div>

  <div class="abs card" style="left:720px;top:2551px">
    <div class="card-name">Owen Harker</div>
    <div class="card-role">Manager of <em>Marlow Studio</em></div>
    <p class="card-text">Lorem ipsum dolor sit amet, consectetur adipisicing elit, sed do eiusmod tempor incididunt ut labore et dolore magna quis aliqua. Ut enim ad minim veniam, quis nostrud exercitation ullamco laboris nisi ...</p>
    <div class="card-more" style="top:166px">Read all</div>
  </div>
  <div class="abs avatar" style="left:650px;top:2603px;background:linear-gradient(160deg,#a88a6c,#4d3a2e)" role="img" aria-label="Portrait of Owen Harker"></div>

  <div class="abs view-all">View All.</div>
</section>

<section>
  <h2 class="abs h2 book-title">BOOK A RATEABLE VALUATION WITH ONE OF OURS QUALIFIED SURVEYORS</h2>
  <div class="abs btn" style="left:506px;top:2918px;width:188px;height:53px">BOOK&nbsp; VALUATION NOW</div>
</section>

<footer>
  <div class="abs footer" role="img" aria-label="Faint dark city skyline"></div>
  <div class="abs foot-links">
    <p>LOCATION</p>
    <p class="addr">Kestle House<br>Quayside Park<br>Manchester, M99 4QX</p>
    <p>PRICING PLAN</p>
    <p>ABOUT US</p>
    <p>FAQS</p>
    <p>LEGAL &amp; TERMS</p>
    <p>FOLLOW US</p>
    <p class="social"><svg width="10" height="10" viewBox="0 0 10 10" fill="none" stroke="#1479b0" stroke-width="1.5"><path d="M1 1l4 4-4 4M5 1l4 4-4 4"/></svg>NETWORK</p>
    <p class="social"><svg width="10" height="10" viewBox="0 0 10 10" fill="none" stroke="#1479b0" stroke-width="1.5"><path d="M1 1l4 4-4 4M5 1l4 4-4 4"/></svg>COMMUNITY</p>
    <p class="social"><svg width="10" height="10" viewBox="0 0 10 10" fill="none" stroke="#1479b0" stroke-width="1.5"><path d="M1 1l4 4-4 4M5 1l4 4-4 4"/></svg>UPDATES</p>
  </div>
  <div class="abs form">
    <div class="form-title">GET IN TOUCH WITH US</div>
    <div class="field" style="top:62px;height:37px">Name:</div>
    <div class="field" style="top:107px;height:36px">E-mail:</div>
    <div class="field" style="top:151px;height:74px">Message:</div>
    <div class="submit">SUBMIT</div>
  </div>
  <div class="abs bottom-bar">PLINTHMOOR ASSESSMENTS ALL RIGHTS RESERVED 2019.&nbsp;&nbsp;PRIVACY POLICY.</div>
</footer>
</body>
</html>
```